Zelvo - revolutionary mobile payment

The app is a P2P money trasfert, without the using of credit card or bank circuits it can transfer electronic money from one person to another consumers simply and immediatelly.
You can use the color you want, but the message we need to transert to consumer is simplicity, safety and coolness.
In attach the logo of the company and the wireframe of thre page of the app.
The goal is to design the page of the app with a clear, simple and intuitive graphic.
Updates

I have upgrade the brief with important information and detail, many thanks

Target Market(s)

all the people

Industry/Entity Type

Credit Card

Requirements
Must have
• You have to design one icon for each button in the first page, (shop is: where to shop)
in the second one a new intuitive image (instead of the hand) that let the user to understand that with a simple swipe he can process the payment
Nice to have
• You can include or esxclude what you want or belive can improve user experience of the app
Should not have
• too much color, too much button or information

```html
<!DOCTYPE html>
<html lang="it">
<head>
<meta charset="utf-8">
<title>Zelvo – Pay</title>
<link rel="stylesheet" href="https://fonts.googleapis.com/css2?family=Questrial&family=Montserrat:wght@600;700&display=swap">
<style>
  :root {
    --canvas: #c4c7cb;
    --black: #0d0d0d;
    --bar-dark: #3a3b3d;
    --bar-mid: #5b5c5e;
    --band-light: #f2f2f2;
    --band-grey: #bdbdbd;
    --field-dark: #4a4a4a;
    --key-dark: #1c1c1c;
    --key-line: #5a5a5a;
    --accent: #e0520e;
    --accent-soft: #f08a3a;
    --ink: #111111;
    --white: #ffffff;
    --brand-blue: #2b5aa8;
  }
  * { box-sizing: border-box; margin: 0; padding: 0; }
  html, body { width: 1200px; height: 1195px; overflow: hidden; background: var(--canvas); }
  body { position: relative; font-family: "Questrial", sans-serif; }

  .app-screen {
    position: absolute; left: 300px; top: 64px;
    width: 600px; height: 1066px;
    background: var(--black);
    overflow: hidden;
    display: flex; flex-direction: column;
    box-shadow: 0 20px 50px rgba(0,0,0,.25);
  }

  .status-bar {
    height: 38px; background: var(--black); color: var(--white);
    display: flex; align-items: center; justify-content: space-between;
    padding: 0 14px; font-size: 17px; font-family: "Montserrat", sans-serif; font-weight: 600;
  }
  .status-bar .carrier { display: flex; align-items: center; gap: 6px; }
  .status-bar .battery { display: flex; align-items: center; gap: 8px; }
  .battery-icon { width: 36px; height: 16px; border: 2px solid var(--white); border-radius: 3px; position: relative; }
  .battery-icon::before { content: ""; position: absolute; left: 1px; top: 1px; bottom: 1px; width: 7px; background: var(--white); }

  .nav-bar {
    height: 72px;
    background: linear-gradient(90deg, var(--bar-dark), var(--bar-mid));
    display: flex; align-items: center; justify-content: flex-end; padding: 0 22px;
  }
  .brand { display: flex; align-items: center; gap: 8px; color: var(--white); font-size: 26px; }
  .brand-dot { width: 22px; height: 22px; border-radius: 50%; background: var(--brand-blue); }

  .title-band {
    height: 92px;
    background: linear-gradient(180deg, var(--band-light), var(--band-grey));
    display: flex; align-items: center; justify-content: center; position: relative;
  }
  .settings { position: absolute; left: 20px; top: 50%; transform: translateY(-50%); }
  .page-title { display: flex; align-items: center; gap: 14px; font-family: "Montserrat", sans-serif; font-weight: 700; font-size: 40px; color: var(--white); text-shadow: 0 1px 3px rgba(0,0,0,.55); }

  .payment-area {
    flex: 1; display: flex; flex-direction: column;
    background:
      radial-gradient(circle at 30% 8%, rgba(240,138,58,.95) 0, rgba(240,138,58,0) 32%),
      radial-gradient(circle at 85% 30%, rgba(224,82,14,.75) 0, rgba(224,82,14,0) 30%),
      radial-gradient(circle at 20% 62%, rgba(224,82,14,.55) 0, rgba(224,82,14,0) 30%),
      radial-gradient(circle at 60% 85%, rgba(200,70,10,.4) 0, rgba(200,70,10,0) 28%),
      linear-gradient(180deg, #2a2a2a, #141414);
  }

  .back-row { height: 64px; display: flex; align-items: center; }
  .back-link { color: var(--white); font-size: 22px; padding-left: 20px; width: 160px; }
  .recipient-field {
    flex: 1; margin-right: 18px; height: 44px;
    background: linear-gradient(90deg, rgba(255,255,255,.85), rgba(255,255,255,.35));
    border: 1px solid rgba(255,255,255,.8);
  }

  .recipient-row { height: 70px; display: flex; align-items: center; padding: 0 20px; gap: 14px; }
  .device-icon { width: 58px; height: 58px; background: var(--white); display: flex; align-items: center; justify-content: center; }
  .recipient-label { flex: 1; height: 44px; display: flex; align-items: center; gap: 14px; font-size: 22px; color: var(--ink); background: linear-gradient(90deg, rgba(255,255,255,.25), rgba(255,255,255,0)); padding-left: 6px; }
  .recipient-label .prefix { font-family: "Montserrat", sans-serif; font-weight: 700; font-size: 19px; }

  .amount-row { height: 118px; display: flex; align-items: center; padding: 0 20px; gap: 18px; }
  .currency { font-family: "Montserrat", sans-serif; font-weight: 700; font-size: 44px; color: var(--ink); width: 40px; text-align: center; }
  .amount-field {
    flex: 1; height: 92px; background: rgba(74,74,74,.8);
    display: flex; align-items: center; justify-content: flex-end; padding-right: 28px;
    font-family: "Montserrat", sans-serif; font-weight: 700; font-size: 56px; color: var(--ink); letter-spacing: 3px;
  }

  .notes-row { height: 40px; display: flex; align-items: center; padding-left: 20px; }
  .notes-select { font-size: 15px; color: var(--white); border-bottom: 1px solid rgba(255,255,255,.5); padding: 4px 6px; display: flex; gap: 10px; align-items: center; }

  .keypad {
    flex: 1; margin: 0 0 0 0;
    display: grid; grid-template-columns: repeat(3, 1fr); grid-template-rows: repeat(4, 1fr);
    border-top: 1px solid var(--key-line);
  }
  .key {
    display: flex; align-items: center; justify-content: center;
    font-family: "Montserrat", sans-serif; font-weight: 700; font-size: 42px; color: var(--white);
    background: rgba(20,20,20,.55);
    border-right: 1px solid var(--key-line); border-bottom: 1px solid var(--key-line);
  }
  .key:nth-child(3n) { border-right: none; }
  .key.is-pressed { background: var(--accent); }
</style>
</head>
<body>
  <main class="app-screen">
    <div class="status-bar">
      <span class="carrier">●●●○○ NOVA
        <svg width="20" height="14" viewBox="0 0 20 14"><path d="M1 5a13 13 0 0 1 18 0M4 8a8 8 0 0 1 12 0M7 11a4 4 0 0 1 6 0" stroke="#fff" stroke-width="2" fill="none"/></svg>
      </span>
      <span class="clock">4:21 PM</span>
      <span class="battery">22% <span class="battery-icon"></span></span>
    </div>

    <header class="nav-bar">
      <div class="brand"><span class="brand-dot"></span>Zelvo</div>
    </header>

    <div class="title-band">
      <svg class="settings" width="32" height="32" viewBox="0 0 32 32" aria-label="Impostazioni">
        <g fill="#333"><circle cx="16" cy="16" r="9"/>
        <rect x="13" y="2" width="6" height="28" rx="1"/><rect x="2" y="13" width="28" height="6" rx="1"/>
        <rect x="13" y="2" width="6" height="28" rx="1" transform="rotate(45 16 16)"/><rect x="13" y="2" width="6" height="28" rx="1" transform="rotate(-45 16 16)"/></g>
        <circle cx="16" cy="16" r="4" fill="#ddd"/>
      </svg>
      <h1 class="page-title">
        <svg width="40" height="40" viewBox="0 0 40 40" aria-hidden="true">
          <circle cx="20" cy="20" r="17" fill="none" stroke="#fff" stroke-width="4"/>
          <path d="M12 20h14M20 13l7 7-7 7" stroke="#fff" stroke-width="4" fill="none" stroke-linecap="round" stroke-linejoin="round"/>
        </svg>
        Pay
      </h1>
    </div>

    <section class="payment-area" role="img" aria-label="Sfondo sfocato in toni arancio e grigio scuro">
      <div class="back-row">
        <span class="back-link">‹ Indietro</span>
        <span class="recipient-field"></span>
      </div>

      <div class="recipient-row">
        <span class="device-icon">
          <svg width="34" height="34" viewBox="0 0 34 34"><rect x="3" y="4" width="28" height="26" rx="3" fill="none" stroke="#111" stroke-width="3"/><rect x="8" y="9" width="18" height="14" fill="#111"/></svg>
        </span>
        <span class="recipient-label"><span class="prefix">+39</span>Cellulare</span>
      </div>

      <div class="amount-row">
        <span class="currency">€</span>
        <span class="amount-field">851.33</span>
      </div>

      <div class="notes-row">
        <span class="notes-select">Inserisci note (opzionale) <span>▾</span></span>
      </div>

      <div class="keypad">
        <span class="key">1</span>
        <span class="key">2</span>
        <span class="key">3</span>
        <span class="key">4</span>
        <span class="key">5</span>
        <span class="key">6</span>
        <span class="key">7</span>
        <span class="key is-pressed">8</span>
        <span class="key">9</span>
        <span class="key">.</span>
        <span class="key">0</span>
        <span class="key" aria-label="Cancella">
          <svg width="52" height="32" viewBox="0 0 52 32"><path d="M14 2h36v28H14L2 16z" fill="#fff"/><path d="M26 10l12 12M38 10L26 22" stroke="#1c1c1c" stroke-width="4" stroke-linecap="round"/></svg>
        </span>
      </div>
    </section>
  </main>
</body>
</html>
```